Tri-fold Brochure, Postcard & Letterhead Design | ||
Small Engineering Consulting & Services Firm for Building Energy Efficiency | ||
I want to have tri-fold brochure and postcard designs that can represent our company well. Our company is providing engineering consulting and services to improve energy efficiency of building mechanical systems and thus reduce energy consumptions of large commercial buildings. The details of the company information can be found in the website: www.corvalith.com, and any questions about the can be routed to tkal@corvalith.com. I have my company logo and biz card design in different format (originally designed by Emblem Craft Hub) and provide them to designers upon request. | ||
Building owners and facility managers of commercial, institutional and industrial buildings, including large office buildings, hospitals, schools and university campuses, data centers, etc. | ||
The tri-fold brochure and postcard should be designed in a way that its contents can be editable in MS Publisher or Word. The letter head can be designed for use in MS Word. |
HVAC_system_solutions_728.jpg Hello, designers! As posted in our website www.corvalith.com, our company is providing services to improve building energy efficiency. Our customers are building owners, facility managers and operators. The real focus of our business is to optimize the operation of building mechanical systems. We don't do the lighting ourselves and typically oursource the lighting portion. In a building, mechanical systems consume more than 50% of energy for heating, ventilating and air-conditioning. So I would like to have images related to the building mechanical systems. You may google images of "HVAC", "chillers", "AHU", and/or "building automation systems". I will upload some samples from google images. I hope it can help. Thanks, |
CORVALITH_23480_FinalLogo_D4L4_714.jpg Use the uploaded logo and also reference the business card design. To understand the company's services and characters, check out the company website at www.corvalith.com |

```html
<!DOCTYPE html>
<html lang="en">
<head>
<meta charset="utf-8">
<title>CORVALITH Tri-fold Brochure – Inside</title>
<link href="https://fonts.googleapis.com/css2?family=Libre+Baskerville:ital,wght@0,700;1,400;1,700&family=Arimo:ital,wght@0,400;0,700;1,400&display=swap" rel="stylesheet">
<style>
  :root{
    --navy:#1d3f7a;
    --ink:#222;
    --green:#1fa24a;
    --green-dark:#0f7d3a;
    --green-light:#5cc46a;
    --paper:#ffffff;
  }
  *{margin:0;padding:0;box-sizing:border-box}
  html,body{width:1200px;height:961px;overflow:hidden;background:var(--paper)}
  .brochure{position:relative;width:1200px;height:961px;font-family:"Arimo",Arial,sans-serif;color:var(--ink)}
  .panel{position:absolute;top:0;width:400px;height:961px}
  .panel--services{left:0}
  .panel--retrofits{left:400px}
  .panel--procedure{left:800px}
  .panel-title{position:absolute;left:40px;top:18px;height:40px;font-family:"Libre Baskerville",Georgia,serif;font-weight:700;font-style:italic;font-size:31px;line-height:40px;color:var(--navy)}
  .panel-title::after{content:"";position:absolute;left:0;top:44px;width:330px;height:6px;border-top:2px solid var(--green);border-bottom:2px solid var(--green)}
  .panel--retrofits .panel-title{left:30px}
  .panel--retrofits .panel-title::after{display:none}
  .subtitle{position:absolute;left:30px;top:64px;width:345px;font-family:"Libre Baskerville",Georgia,serif;font-weight:700;font-style:italic;font-size:15px;line-height:21px;color:var(--navy)}
  .intro{position:absolute;left:40px;top:78px;width:330px;font-style:italic;font-size:14px;line-height:20px;text-align:justify}
  .intro b{font-style:normal}
  .service-list{position:absolute;left:30px;top:228px;width:340px;list-style:none;font-style:italic;font-size:14.5px;line-height:22px}
  .service-list li{position:relative;padding-left:46px;margin-bottom:28px}
  .service-list li::before{content:"\2666";position:absolute;left:0;top:0;font-style:normal;color:#333}
  .city-art{position:absolute;left:14px;top:660px;width:372px;height:235px;background:linear-gradient(180deg,#dfe9f6 0%,#8fb3dc 55%,#3d6ea8 100%)}
  .benefits{position:absolute;left:30px;top:160px;width:335px;font-style:italic;font-size:14.5px;line-height:21px;text-align:justify}
  .benefits p{position:relative;text-indent:46px;margin-bottom:22px}
  .benefits p::before{content:"\2666";position:absolute;left:-46px;top:0;font-style:normal}
  .bas-diagram{position:absolute;left:30px;top:500px;width:380px;height:395px;background:linear-gradient(180deg,#eef1f5 0%,#cfd6df 100%)}
  .phases{position:absolute;left:40px;top:76px;width:340px;font-size:12.5px;line-height:16px}
  .phase{margin-bottom:14px}
  .phase h3{font-family:"Arimo",Arial,sans-serif;font-weight:700;font-size:14px;line-height:18px;color:var(--green-dark)}
  .phase h3 span{display:block}
  .phase--mv{width:160px}
  .bar-chart{position:absolute;left:205px;top:485px;width:170px;height:175px}
  .line-chart{position:absolute;left:113px;top:668px;width:272px;height:222px}
  .footer-band{position:absolute;left:0;bottom:0;width:1200px;height:58px;background:var(--green)}
  .footer-band::before{content:"";position:absolute;left:0;top:-8px;width:1200px;height:8px;background:var(--green-dark)}
  .footer-band .mid{position:absolute;left:400px;top:0;width:400px;height:58px;background:var(--green-light)}
</style>
</head>
<body>
<div class="brochure">

  <section class="panel panel--services">
    <h2 class="panel-title">Services</h2>
    <p class="intro"><b>CORVALITH’s</b> highly educated and experienced staff can provide any and all of the following services with special attention to the type of facility. The uniqueness of each facility type requires the correct expertise to meet both thermal comfort requirements and the need for energy efficiency.</p>
    <ul class="service-list">
      <li>HVAC Engineering Consulting</li>
      <li>Investment Grade Energy Audits</li>
      <li>New Building Commissioning and</li>
      <li>Re-Commissioning</li>
      <li>Building Retrofits and Integrated Energy System Commissioning and Optimization (BRISCO: see below)</li>
      <li>Energy Star Certification</li>
      <li>Measurement and Verification (M&amp;V)</li>
      <li>Training and Documentation</li>
    </ul>
    <div class="city-art" role="img" aria-label="Blue illustration of a city skyline with office towers and energy systems"></div>
  </section>

  <section class="panel panel--retrofits">
    <h2 class="panel-title">Building Retrofits</h2>
    <p class="subtitle">and Integrated System Commissioning and Optimization (BRISCO)</p>
    <div class="benefits">
      <p>Technologies that not only manage building retrofits and energy commissioning but also integrate optimization methodologies and monitor operation and energy uses for maximum energy efficiency.</p>
      <p>Energy efficiency improvement technologies that use ‘Continuous Commissioning Guidebook’ published in Federal Energy Management Program (FEMP) as minimum requirements.</p>
      <p>Custom algorithms designed and implemented in the clients’ existing control systems to provide sustainable energy savings.</p>
    </div>
    <div class="bas-diagram" role="img" aria-label="Building automation system diagram with workstations, controllers and networked HVAC equipment"></div>
  </section>

  <section class="panel panel--procedure">
    <h2 class="panel-title">Procedure</h2>
    <div class="phases">
      <div class="phase">
        <h3><span>Phase 1:</span>Preliminary Studies</h3>
        <p>1. Compare and analyze energy use data by building types.<br>2. Use Energy Star, ASHRAE Standard 90.1<br>3. Preliminary walk-through.<br>4. Evaluate economic values of the projects.</p>
      </div>
      <div class="phase">
        <h3><span>Phase 2:</span>Energy Audits</h3>
        <p>1. Collect and analyze existing documents.<br>2. Interview with site staffs.<br>3. On-site evaluation for 2~5 days<br>4. Calculate energy savings<br>5. Provide audit reports and proposals</p>
      </div>
      <div class="phase">
        <h3><span>Phase 3:</span>Implementation</h3>
        <p>1. Kick-off meeting with onsite staff’s approval<br>2. Retrofit specs, bids, installations<br>3. Functional tests for new equipment<br>4. Optimization and custom algorithm<br>5. End-of-work report</p>
      </div>
      <div class="phase phase--mv">
        <h3><span>Phase 4:</span>M&amp;V</h3>
        <p>1. Immediate checks for results<br>2. Seasonal check-ups<br>3. Long-term M&amp;V for building energy usage<br>4. Final report<br>5. Case studies and benchmarking</p>
      </div>
    </div>

    <svg class="bar-chart" viewBox="0 0 170 180" preserveAspectRatio="none" role="img" aria-label="Monthly energy use bar chart">
      <rect x="0" y="0" width="170" height="180" fill="#f4f6f8" stroke="#bbb"/>
      <text x="85" y="14" font-size="8" text-anchor="middle" fill="#333" font-family="Arimo, sans-serif">Monthly energy use</text>
      <g stroke="#ddd"><line x1="18" y1="40" x2="165" y2="40"/><line x1="18" y1="80" x2="165" y2="80"/><line x1="18" y1="120" x2="165" y2="120"/></g>
      <line x1="18" y1="160" x2="165" y2="160" stroke="#888"/>
      <g fill="#d93a2e">
        <rect x="22" y="45" width="5" height="115"/><rect x="34" y="50" width="5" height="110"/><rect x="46" y="42" width="5" height="118"/>
        <rect x="58" y="55" width="5" height="105"/><rect x="70" y="48" width="5" height="112"/><rect x="82" y="44" width="5" height="116"/>
        <rect x="94" y="52" width="5" height="108"/><rect x="106" y="46" width="5" height="114"/><rect x="118" y="50" width="5" height="110"/>
        <rect x="130" y="43" width="5" height="117"/><rect x="142" y="49" width="5" height="111"/><rect x="154" y="47" width="5" height="113"/>
      </g>
      <g fill="#3d7fc4">
        <rect x="27" y="60" width="4" height="100"/><rect x="39" y="66" width="4" height="94"/><rect x="51" y="58" width="4" height="102"/>
        <rect x="63" y="70" width="4" height="90"/><rect x="75" y="64" width="4" height="96"/><rect x="87" y="60" width="4" height="100"/>
        <rect x="99" y="68" width="4" height="92"/><rect x="111" y="62" width="4" height="98"/><rect x="123" y="66" width="4" height="94"/>
        <rect x="135" y="59" width="4" height="101"/><rect x="147" y="65" width="4" height="95"/><rect x="159" y="63" width="4" height="97"/>
      </g>
    </svg>

    <svg class="line-chart" viewBox="0 0 272 225" preserveAspectRatio="none" role="img" aria-label="Daily total electricity profile line chart">
      <rect x="0" y="0" width="272" height="225" fill="#fff" stroke="#bbb"/>
      <text x="140" y="14" font-size="10" font-weight="700" text-anchor="middle" fill="#222" font-family="Arimo, sans-serif">Daily total electricity profile</text>
      <rect x="60" y="20" width="160" height="12" fill="none" stroke="#999"/>
      <line x1="64" y1="26" x2="76" y2="26" stroke="#2f9e44" stroke-width="2"/>
      <text x="79" y="29" font-size="7" font-family="Arimo, sans-serif" fill="#333">Pre-Implementation</text>
      <line x1="142" y1="26" x2="154" y2="26" stroke="#d93a2e" stroke-width="2"/>
      <text x="157" y="29" font-size="7" font-family="Arimo, sans-serif" fill="#333">Post-Implementation</text>
      <g stroke="#e3e3e3">
        <line x1="30" y1="50" x2="265" y2="50"/><line x1="30" y1="80" x2="265" y2="80"/><line x1="30" y1="110" x2="265" y2="110"/>
        <line x1="30" y1="140" x2="265" y2="140"/><line x1="30" y1="170" x2="265" y2="170"/>
      </g>
      <line x1="30" y1="200" x2="265" y2="200" stroke="#777"/>
      <line x1="30" y1="40" x2="30" y2="200" stroke="#777"/>
      <g font-size="6.5" fill="#444" font-family="Arimo, sans-serif" text-anchor="end">
        <text x="27" y="52">900</text><text x="27" y="82">800</text><text x="27" y="112">700</text>
        <text x="27" y="142">600</text><text x="27" y="172">500</text><text x="27" y="202">400</text>
      </g>
      <g font-size="6.5" fill="#444" font-family="Arimo, sans-serif" text-anchor="middle">
        <text x="30" y="211">0:00</text><text x="89" y="211">6:00</text><text x="148" y="211">12:00</text><text x="206" y="211">18:00</text><text x="258" y="211">24:00</text>
      </g>
      <text x="148" y="221" font-size="7" text-anchor="middle" fill="#333" font-family="Arimo, sans-serif">Hour of the day</text>
      <polyline fill="none" stroke="#2f9e44" stroke-width="1.6" points="30,150 45,152 60,149 75,146 85,120 95,75 110,62 130,58 150,56 170,60 190,58 205,64 215,90 225,128 240,140 255,146 265,148"/>
      <polyline fill="none" stroke="#d93a2e" stroke-width="1.6" points="30,168 45,170 60,167 75,164 85,145 95,100 110,90 130,86 150,84 170,88 190,87 205,92 215,118 225,150 240,160 255,164 265,166"/>
    </svg>
  </section>

  <div class="footer-band"><div class="mid"></div></div>
</div>
</body>
</html>
```